Short term Rentals Marketing agency needs Web design.

We Need a web design for our new company based in Calgary, AB. We are a International Luxury home sharing company (short term rental properties, Villas, Boutique Hotels, Bed & Breakfast, Realtors, Mortgage Brokers). We would like to see designs that look simple, modern and professional. Colors would be bold (red, black, white). The final design should communicate something welcoming, symbolize innovation, and growth. Our goal is to form partnerships with Real Estate, Property Management, Short term Rental Clients to make their lives easier and increase revenue. Vlto Harbor Co. offers a flexible and secure way to market our clients properties while maintaining client satisfaction and amazing customer service. We like how https://brinkleafpromo.ca/ is interactive (when you scroll down, text gets larger). Other similar websites for Short Term Rentals is https://www.quillnestgroup.com/, https://dwelvaroo.com/, https://www.kipmarsh.com/, https://www.tarnpenny.com/about-us/, https://vantrelstays.com. We have attached our Logo.

Target Market(s)

short term rental properties, Villas, Boutique Hotels, Bed & Breakfast, Realtors, Mortgage Brokers, property owners

Industry/Entity Type

Real Estate

Coding

Coded - Design and coding required

Number of Pages Required

5+ page

Font styles to use
Sans Serif

Requirements
Must have
• Home Page, About Us page, How it works, Services, Contact us.

We like how https://brinkleafpromo.ca/ is interactive (when you scroll down, text gets larger).

We have attached our Webcopy. We would like Call to Action Buttons where they're located in the copy and page.

Must have our Logo Colors.

Other similar websites for Short Term Rentals is https://www.quillnestgroup.com/, https://dwelvaroo.com/, https://www.kipmarsh.com/, https://www.tarnpenny.com/about-us/, https://vantrelstays.com.
Nice to have
• Catchy, Interactive Home page.

Should not have
• Should not be too cluttered

```html
<!DOCTYPE html>
<html lang="en">
<head>
<meta charset="utf-8">
<title>Vlto Harbor Co. — Short-Term Rental Management</title>
<link href="https://fonts.googleapis.com/css2?family=Poppins:wght@300;400;500;600;700&display=swap" rel="stylesheet">
<style>
  :root {
    --red: #e3202a;
    --ink: #1b1b22;
    --muted: #5d5f6a;
    --white: #ffffff;
    --footer-bg: #eceef2;
    --card-bg: #fbfbfc;
  }
  * { box-sizing: border-box; margin: 0; padding: 0; }
  html, body { width: 791px; height: 1200px; overflow: hidden; }
  body { font-family: "Poppins", sans-serif; color: var(--ink); background: var(--white); position: relative; }

  .hero {
    position: absolute; left: 0; top: 0; width: 791px; height: 395px;
    background:
      linear-gradient(180deg, rgba(60,80,110,.25) 0%, rgba(20,25,40,.1) 50%, rgba(15,18,22,.55) 100%),
      linear-gradient(180deg, #6b8db8 0%, #8ea3bf 28%, #aab3c2 45%, #8d8a86 58%, #c89a55 66%, #4d524c 76%, #2f3330 100%);
  }
  .brand { position: absolute; left: 32px; top: 18px; display: flex; align-items: center; gap: 7px; color: var(--white); }
  .brand-mark { width: 22px; height: 22px; border: 3px solid var(--white); }
  .brand-name { font-size: 17px; font-weight: 500; line-height: 1; letter-spacing: .2px; }

  .nav a { position: absolute; top: 34px; font-size: 8.5px; color: var(--white); text-decoration: none; }
  .cta-consult {
    position: absolute; left: 622px; top: 28px; width: 137px; height: 23px; border-radius: 12px;
    background: var(--red); color: var(--white); font-size: 8.6px; font-weight: 600;
    display: flex; align-items: center; justify-content: center; gap: 5px;
  }
  .hero-title { position: absolute; left: 0; top: 128px; width: 791px; text-align: center; color: var(--white); }
  .hero-title .light { display: block; font-size: 25.5px; font-weight: 400; line-height: 31px; }
  .hero-title .bold { display: block; font-size: 26px; font-weight: 700; line-height: 30px; }
  .btn-outline {
    position: absolute; width: 95px; height: 23px; border-radius: 12px; border: 1.2px solid var(--white);
    color: var(--white); font-size: 8.5px; font-weight: 500; display: flex; align-items: center; justify-content: center;
  }
  .hero .btn-outline { left: 348px; top: 210px; }

  .intro { position: absolute; left: 192px; top: 444px; width: 406px; font-size: 9.4px; line-height: 15.8px; color: #4a4c55; text-align: justify; }
  .wordmark { position: absolute; left: 80px; top: 540px; }
  .details { position: absolute; left: 192px; top: 629px; width: 406px; font-size: 7.3px; line-height: 12.6px; color: #4a4c55; text-align: justify; }
  .details p + p { margin-top: 12.6px; }

  .card { position: absolute; top: 766px; width: 196px; height: 290px; background: var(--card-bg); }
  .card.is-featured { background: var(--white); box-shadow: 0 4px 18px rgba(0,0,0,.06); }
  .card-art { position: absolute; left: 30px; top: 12px; width: 136px; height: 128px; border-radius: 50%; }
  .card-title { position: absolute; left: 0; top: 150px; width: 196px; text-align: center; font-size: 12.6px; font-weight: 500; line-height: 15.5px; }
  .card-body { position: absolute; left: 20px; top: 192px; width: 156px; font-size: 7.3px; line-height: 13.7px; color: var(--muted); text-align: justify; }
  .card-arrow {
    position: absolute; left: 85px; top: 272px; width: 27px; height: 27px; border-radius: 50%;
    background: var(--white); box-shadow: 0 2px 8px rgba(0,0,0,.06);
    display: flex; align-items: center; justify-content: center;
  }
  .card.is-featured .card-arrow { background: var(--red); }

  .btn-work { left: 348px; top: 1092px; border-color: var(--red); color: var(--red); }

  .footer { position: absolute; left: 0; top: 1158px; width: 791px; height: 42px; background: var(--footer-bg); }
  .footer-mark { position: absolute; left: 87px; top: 12px; width: 17px; height: 17px; border: 2.5px solid var(--red); }
  .footer-copy { position: absolute; left: 111px; top: 15px; font-size: 7.6px; color: var(--muted); }
  .social { position: absolute; top: 14px; width: 10px; height: 10px; background: #7a7d88; border-radius: 1px; }
</style>
</head>
<body>

<header class="hero" role="img" aria-label="Dusk photograph of a modern desert vacation home with lit windows among Joshua trees">
  <div class="brand"><span class="brand-mark"></span><span class="brand-name">Vlto Harbor Co.</span></div>
  <nav class="nav">
    <a style="left:301px">Home</a>
    <a style="left:355px">About</a>
    <a style="left:411px">How it Works</a>
    <a style="left:494px">Services</a>
    <a style="left:558px">Contact</a>
  </nav>
  <div class="cta-consult">
    <svg width="9" height="8" viewBox="0 0 9 8"><path d="M0 3 L4.5 0 L9 3 V8 H0 Z" fill="#fff"/><path d="M0.5 3.3 L4.5 5.6 L8.5 3.3" stroke="#e3202a" stroke-width=".9" fill="none"/></svg>
    Request Consultation
  </div>
  <h1 class="hero-title"><span class="light">Partner with Us and Let’s Start</span><span class="bold">Growing Together!</span></h1>
  <div class="btn-outline">Work With Us</div>
</header>

<p class="intro">Vlto Harbor Co. is here to manage and market your short-term rental properties so you don’t have to. Enjoy peace of mind in knowing your short-term rental properties, vacation homes, villas, hotels, and B&amp;Bs are safe, secure, and profitable – no matter where you are in the world. We will help you market, manage, and capitalize on everything, from your newest bookings to house cleaning and upkeep.</p>

<svg class="wordmark" width="632" height="80" viewBox="0 0 632 80" aria-hidden="true">
  <text x="7" y="61" font-family="Poppins, sans-serif" font-size="72" font-weight="500" fill="none" stroke="#e3202a" stroke-width=".8" textLength="618" lengthAdjust="spacingAndGlyphs">VLTO Harbor CO</text>
</svg>

<div class="details">
  <p>Vlto Harbor Co. saves you time, money, and effort, so that you can focus on the things that matter most to you. Let us help you increase your rental revenue in a simple and hassle-free way by increasing your occupancy, streamlining your bookings, getting you amazing exposure, and keeping your property looking incredible year-round.</p>
  <p>Read on to find out what we can do for you when we manage and market your vacation or shortterm rental property.</p>
</div>

<article class="card is-featured" style="left:87px">
  <div class="card-art" role="img" aria-label="Illustration of rising bar chart with gold coin and gears" style="background:radial-gradient(circle at 50% 50%, #c9a2ec 0%, #eee8f6 60%, #fbfbfc 75%)"></div>
  <h2 class="card-title">Increase Your<br>Revenue</h2>
  <p class="card-body">Having Vlto Harbor Co. manage and market your rental property lets you benefit from increased revenues without having to put in the hours of work yourself.</p>
  <div class="card-arrow"><svg width="9" height="8" viewBox="0 0 9 8"><path d="M0 4 H8 M5 1 L8 4 L5 7" stroke="#fff" stroke-width="1.2" fill="none"/></svg></div>
</article>

<article class="card" style="left:298px">
  <div class="card-art" role="img" aria-label="Illustration of round-the-clock support on a laptop with gears" style="background:radial-gradient(circle at 50% 50%, #f19a8f 0%, #b58ad8 35%, #ececf2 62%, #fbfbfc 75%)"></div>
  <h2 class="card-title">Receive Constant<br>Support</h2>
  <p class="card-body">Our affordable and professional services include being there to support your guests, constant technical communication, and on-site operations management.</p>
  <div class="card-arrow"><svg width="9" height="8" viewBox="0 0 9 8"><path d="M0 4 H8 M5 1 L8 4 L5 7" stroke="#e3202a" stroke-width="1.2" fill="none"/></svg></div>
</article>

<article class="card" style="left:509px">
  <div class="card-art" role="img" aria-label="Illustration of an orange umbrella sheltering a figure in front of a gear" style="background:radial-gradient(circle at 50% 40%, #f6a23a 0%, #f3c27c 30%, #e6e7ee 60%, #fbfbfc 75%)"></div>
  <h2 class="card-title">Manage Your Risks<br>&amp; Insurance</h2>
  <p class="card-body">Vlto Harbor Co. will help you protect your property income by giving you the security and insurance you need when it comes to pricing and managing your security deposits.</p>
  <div class="card-arrow"><svg width="9" height="8" viewBox="0 0 9 8"><path d="M0 4 H8 M5 1 L8 4 L5 7" stroke="#e3202a" stroke-width="1.2" fill="none"/></svg></div>
</article>

<div class="btn-outline btn-work">Work With Us</div>

<footer class="footer">
  <span class="footer-mark"></span>
  <span class="footer-copy">© Vlto Harbor Co. All Rights Reserved.</span>
  <span class="social" style="left:642px"></span>
  <span class="social" style="left:659px"></span>
  <span class="social" style="left:676px"></span>
  <span class="social" style="left:693px"></span>
</footer>

</body>
</html>
```